New young doctors office business card

Doctor's office
Hello:
My name is Dr. Mateo Anselmo Quiroga Benítez. I need a business card for my new office located within a hospital. The name of the hospital is "Hospital Almendral". Although the hospital logo and name must be included in the business card, please make me a personal logo for myself. The logo might be maybe my name in a stylish font, or my initials (MAQB) or something like that. Im more inclined to a font logo, rather than a image logo, but a good one might change my mind. The info on my business card is going to be in spanish. The following info must be included please (the info within parenthesis is not to be included, it is provided for you to understand it since it's in spanish, so you can properly place it on the card):
-Dr. Mateo Anselmo Quiroga Benítez (my name)
-Medicina general (My specialty)
-Hospital Almendral (The name of the hospital where my office is)
-Calle Tomás Ibarrola #527 Col. Peñascal (address)
-Tel 471-5836 (Office phone)
-Sábado y domingo 10:00 am a 10:00pm (Office hours)
-Emergencias: 613-907-5148 (Emergency phone)
-mateoqb@correoandino.net (email)
-English Spoken
So, that's all the info i need to be on the business card. Although it's a business card for a doctor's office, i dont want it to be a boring, plain business card. Make it eye-catchy and stylish please. As i said, the hospital logo must be included. You'll find it on the heading of the PDF file i attached, but dont make it the center of attention.
Physician
Hello:My name is Dr. Mateo Anselmo Quiroga Benítez. I need a business card for my new office located within a hospital. The name of the hospital is "Hospital Almendral". Although the hospital logo and name must be included in the business card, please make me a personal logo for myself. The logo might be maybe my name in a stylish font, or my initials (MAQB) or something like that. Im more inclined to a font logo, rather than a image logo, but a good one might change my mind. The info on my business card is going to be in spanish. The following info must be included please (the info within parenthesis is not to be included, it is provided for you to understand it since it's in spanish, so you can properly place it on the card):-Dr. Mateo Anselmo Quiroga Benítez (my name)-Medicina general (My specialty)-Hospital Almendral (The name of the hospital where my office is)-Calle Tomás Ibarrola #527 Col. Peñascal (address)-Tel 471-5836 (Office phone)-Sábado y domingo 10:00 am a 10:00pm (Office hours)-Emergencias: 613-907-5148 (Emergency phone)-mateoqb@correoandino.net (email)-English Spoken So, that's all the info i need to be on the business card. Although it's a business card for a doctor's office, i dont want it to be a boring, plain business card. Make it eye-catchy and stylish please. As i said, the hospital logo must be included. You'll find it on the heading of the PDF file i attached, but dont make it the center of attention.

```html
<!DOCTYPE html>
<html lang="es">
<head>
<meta charset="utf-8">
<title>Tarjeta de presentación — Dr. Mateo Anselmo Quiroga Benítez</title>
<link rel="stylesheet" href="https://fonts.googleapis.com/css2?family=Oswald:wght@400;600;700&family=Roboto:ital,wght@0,400;0,500;1,400&display=swap">
<style>
  :root {
    --navy: #2b3c92;
    --navy-deep: #223179;
    --paper: #ffffff;
    --ink: #3b3b3b;
    --mist: #eef0f3;
    --backdrop: #2c2e33;
  }
  * { box-sizing: border-box; margin: 0; padding: 0; }
  html, body {
    width: 1200px; height: 900px; overflow: hidden;
    background: var(--backdrop);
  }
  .stage {
    position: relative; width: 1200px; height: 900px;
  }
  .card {
    position: absolute; left: 300px; width: 600px; height: 343px;
    border-radius: 22px; overflow: hidden;
  }

  /* Front */
  .card-front { top: 60px; background: var(--paper); color: var(--ink); }
  .medical-pattern {
    position: absolute; left: 240px; top: 18px; width: 340px; height: 250px;
    background: radial-gradient(ellipse at center, var(--mist) 0%, rgba(238,240,243,0) 72%);
  }
  .hospital-mark {
    position: absolute; left: 34px; top: 28px;
    display: flex; align-items: center; gap: 10px;
  }
  .hospital-mark .mark-square {
    width: 34px; height: 34px; background: var(--navy);
  }
  .hospital-mark .mark-name {
    font-family: "Oswald", sans-serif; font-weight: 600; font-size: 19px;
    color: var(--navy); text-transform: uppercase; letter-spacing: .5px;
  }
  .contact-list {
    position: absolute; left: 34px; top: 104px; list-style: none;
    font-family: "Roboto", sans-serif; font-size: 15px; color: var(--ink);
  }
  .contact-list li {
    display: flex; align-items: center; gap: 10px; height: 26px;
  }
  .contact-list svg { width: 16px; height: 16px; fill: var(--navy); flex: none; }
  .contact-list .icon-outline { fill: none; stroke: var(--navy); stroke-width: 1.8; }
  .hospital-block {
    position: absolute; right: 36px; top: 150px; text-align: right;
  }
  .hospital-name {
    font-family: "Oswald", sans-serif; font-weight: 700; font-size: 34px;
    color: var(--navy); text-transform: uppercase; line-height: 1.1;
  }
  .hospital-address {
    font-family: "Roboto", sans-serif; font-size: 17px; color: var(--ink);
    margin-top: 4px;
  }
  .hours-band {
    position: absolute; left: 186px; right: 0; bottom: 30px; height: 40px;
    background: var(--navy); color: var(--paper);
    font-family: "Roboto", sans-serif; font-size: 19px;
    display: flex; align-items: center; padding-left: 24px;
  }

  /* Back */
  .card-back { top: 483px; background: var(--navy); color: var(--paper); }
  .card-back .edge-strip {
    position: absolute; left: 0; right: 0; bottom: 0; height: 16px; background: var(--paper);
  }
  .personal-mark {
    position: absolute; left: 0; right: 0; top: 62px; text-align: center;
    font-family: "Oswald", sans-serif; font-weight: 400; font-size: 50px;
    letter-spacing: 6px; color: var(--paper);
  }
  .doctor-name {
    position: absolute; left: 0; right: 0; top: 170px; text-align: center;
    font-family: "Oswald", sans-serif; font-weight: 600; font-size: 27px;
    text-transform: uppercase; letter-spacing: .3px;
  }
  .specialty {
    position: absolute; left: 0; right: 0; top: 214px; text-align: center;
    font-family: "Roboto", sans-serif; font-style: italic; font-size: 17px;
  }
</style>
</head>
<body>
<main class="stage">

  <section class="card card-front" aria-label="Anverso de la tarjeta">
    <div class="medical-pattern" role="img" aria-label="Faint pattern of medical icons: hearts, DNA strands, syringes, stethoscopes, pills"></div>

    <div class="hospital-mark">
      <span class="mark-square"></span>
      <span class="mark-name">Hospital Almendral</span>
    </div>

    <ul class="contact-list">
      <li>
        <svg viewBox="0 0 16 16" aria-hidden="true"><rect class="icon-outline" x="4" y="1.5" width="8" height="13" rx="1.5"/></svg>
        Tel 471-5836
      </li>
      <li>
        <svg viewBox="0 0 16 16" aria-hidden="true"><path d="M4.2 1.5 6.4 4.6 5 6.2c.8 1.9 2.3 3.4 4.2 4.3l1.5-1.4 3.1 2.2-1 2.5C7.5 13.6 2.4 8.5 1.7 3.2Z"/></svg>
        Emergencias: 613-907-5148
      </li>
      <li>
        <svg viewBox="0 0 16 16" aria-hidden="true"><path d="M1 3.5h14v9H1Z M1.6 4l6.4 5 6.4-5" class="icon-outline"/></svg>
        mateoqb@correoandino.net
      </li>
      <li>
        <svg viewBox="0 0 16 16" aria-hidden="true"><path d="M8 2c3.9 0 7 2.4 7 5.4s-3.1 5.4-7 5.4c-.8 0-1.5-.1-2.2-.3L2 14l1.1-3.1C1.8 9.9 1 8.7 1 7.4 1 4.4 4.1 2 8 2Z"/></svg>
        English Spoken
      </li>
    </ul>

    <div class="hospital-block">
      <h2 class="hospital-name">Hospital Almendral</h2>
      <p class="hospital-address">Calle Tomás Ibarrola #527 Col. Peñascal</p>
    </div>

    <div class="hours-band">Sábado y domingo 10:00 am a 10:00pm</div>
  </section>

  <section class="card card-back" aria-label="Reverso de la tarjeta">
    <div class="personal-mark">MAQB</div>
    <h1 class="doctor-name">Dr. Mateo Anselmo Quiroga Benítez</h1>
    <p class="specialty">Medicina general</p>
    <div class="edge-strip"></div>
  </section>

</main>
</body>
</html>
```